New Fun, Positive, energised looking Business Card Needed for High Achiever Coach

I am looking for a two sided full colour business card. I am self employed and have recently re branded my 1-2-1 work Renewing Ambitious Leaders. My target client base for these cards is therefore high achievers - usually aged 40 -55, they are often entrepreneurs, CEO or work in banking and finance and 2/3 are male. I work with them on 90 day or 6 month coaching programs to help them live their success in a healthier, more sustainable and fulfiiled way. They pay for this privately so though they are corporate types the cards need not look 'corporate'. I want to portray the idea of transformation, vitality and re-connecting.
You can get a feel for the look I like on my new website: corinvale.co.uk
I want to use this logo with strapline (Renewing Ambitious Leaders) (I purchased off Logoharbor) and font/ colours (the turquoise and green).
Details to include on the card:
www.corinvale.co.uk
+44 7915 264318
mira@corinvale.co.uk
skype: miracorin
I'd also like to include:
Do you struggle to switch off? Want to be healthier and feel fitter? Want closer relationships? More clarity over the direction you are headed? I can help you do these things using integrated mind-body techniques. Visit corinvale.co.uk TODAY to apply for a FREE Breakthrough session.
BUT if that is too much text for a card I am open to advice/ammendments.
Updates
Thanks for your design - I am considering them. PLease change the wording to :

```html
<!DOCTYPE html>
<html lang="en">
<head>
<meta charset="utf-8">
<title>Mira Corin – Business Card</title>
<link rel="stylesheet" href="https://fonts.googleapis.com/css2?family=Ubuntu:wght@700&family=Alfa+Slab+One&family=Questrial&display=swap">
<style>
  :root {
    --backdrop: #5e3220;
    --turquoise: #1797b8;
    --turquoise-light: #27a9c8;
    --turquoise-deep: #1190b0;
    --green: #5cb85c;
    --paper: #ffffff;
    --paper-edge: #e4e3e4;
    --ink-white: #ffffff;
  }
  * { margin: 0; padding: 0; box-sizing: border-box; }
  html, body { width: 1200px; height: 1181px; overflow: hidden; }
  body { background: var(--backdrop); position: relative; }

  .card {
    position: absolute;
    left: 218px;
    width: 762px;
    height: 437px;
    border-radius: 32px;
    box-shadow: 0 6px 14px rgba(0,0,0,.35);
  }

  /* Front: turquoise message side */
  .card-front {
    top: 113px;
    background: radial-gradient(circle at 50% 52%, var(--turquoise-light) 0%, var(--turquoise-deep) 75%);
    color: var(--ink-white);
    font-family: "Ubuntu", sans-serif;
    font-weight: 700;
    font-size: 13px;
    line-height: 18px;
    text-align: center;
  }
  .front-question { position: absolute; top: 17px; left: 0; right: 0; }
  .front-offer { position: absolute; top: 388px; left: 0; right: 0; }
  .front-mark {
    position: absolute;
    top: 195px; left: 0; right: 0;
    display: flex; align-items: center; justify-content: center; gap: 14px;
    font-size: 34px; line-height: 40px;
  }
  .front-mark .dot { width: 28px; height: 28px; border-radius: 50%; background: var(--ink-white); }

  /* Back: contact side */
  .card-back {
    top: 622px;
    background: radial-gradient(circle at 50% 42%, var(--paper) 0%, var(--paper-edge) 70%);
  }
  .brand {
    position: absolute;
    top: 178px; left: 210px;
    display: flex; align-items: center; gap: 20px;
  }
  .brand-dot { width: 56px; height: 56px; border-radius: 50%; background: var(--green); }
  .brand-name {
    font-family: "Alfa Slab One", serif;
    font-size: 38px; line-height: 42px;
    color: var(--turquoise);
    letter-spacing: 1px;
  }
  .brand-strap {
    font-family: "Questrial", sans-serif;
    font-size: 19px;
    color: var(--turquoise);
    margin-top: 2px;
  }

  .contacts {
    position: absolute;
    top: 375px;
    font-family: "Questrial", sans-serif;
    font-size: 15px;
    line-height: 18px;
    letter-spacing: .4px;
    color: var(--turquoise-deep);
    display: grid;
    grid-template-columns: auto auto;
    column-gap: 6px;
  }
  .contacts dt { color: var(--green); }
  .contacts-left { left: 62px; }
  .contacts-right { left: 485px; }
</style>
</head>
<body>

  <section class="card card-front">
    <p class="front-question">Do you struggle to switch off? Want to be healthier and feel fitter?<br>Want closer relationships? More clarity over the direction you are headed?</p>
    <div class="front-mark"><span class="dot"></span><span>Mira Corin</span></div>
    <p class="front-offer">I can help you do these things using integrated mind-body techniques.<br>Visit corinvale.co.uk TODAY to apply for a FREE Breakthrough session.</p>
  </section>

  <section class="card card-back">
    <div class="brand">
      <span class="brand-dot"></span>
      <div>
        <div class="brand-name">Mira Corin</div>
        <div class="brand-strap">Renewing Ambitious Leaders</div>
      </div>
    </div>

    <dl class="contacts contacts-left">
      <dt>Phone :</dt><dd>+44 7915 264318</dd>
      <dt>skype :</dt><dd>miracorin</dd>
    </dl>
    <dl class="contacts contacts-right">
      <dt>Email&nbsp;&nbsp;:</dt><dd>mira@corinvale.co.uk</dd>
      <dt>Web&nbsp;&nbsp;&nbsp;&nbsp;:</dt><dd>www.corinvale.co.uk</dd>
    </dl>
  </section>

</body>
</html>
```